Stylish business cards for KX7

To create an appealing and professional business card design for a WOMEN Owned Construction Supply Company.
2 sided card. Incorporate brand elements, curvy, colorful, sleek and bright. No solid white background. attached samples of styles added shapes/ribbons. Want something with that WOW that looks awesome, factor. It is a new logo, so feel free to mess with logo colors in the blue and teal factors that can look good with both dark and light background. If you want to try a watermark with just the KX7, without the "Supply" that might look cool to.

Industry/Entity Type

Women owned construction supply company

Contact Information for Business Card

Name, Title, and phone number and email, web page. maybe spot for qr code.

Font styles to use
Sans Serif

Requirements
Nice to have
• would love to see colors, maybe stylish ribbon dividers or some sort of 2 or 3 tone color card that compliments logo.
Should not have
• Please do not have all white background. Do not include Home/reale state/ or building images.

```html
<!DOCTYPE html>
<html lang="en">
<head>
<meta charset="UTF-8">
<title>KX7 Supply — Business Card</title>
<link href="https://fonts.googleapis.com/css2?family=Inter:wght@400;500;600;700&display=swap" rel="stylesheet">
<style>
  :root {
    --page-bg: #dedede;
    --navy: #133758;
    --teal: #0f93b8;
    --white: #ffffff;
    --muted: #a9b0c4;
    --watermark: rgba(30, 80, 110, 0.45);
  }
  * { margin: 0; padding: 0; box-sizing: border-box; }
  html, body {
    width: 1200px; height: 1200px; overflow: hidden;
    background: var(--page-bg);
    font-family: "Inter", sans-serif;
  }
  .card {
    position: absolute;
    left: 179px; width: 861px; height: 495px;
    overflow: hidden;
  }
  .card--front { top: 84px; background: var(--navy); }
  .card--back { top: 622px; background: var(--navy); }

  .brand-name {
    position: absolute;
    font-family: "Inter", sans-serif;
    font-weight: 600;
    white-space: nowrap;
    letter-spacing: 1px;
  }
  .card--front .brand-name {
    left: 0; right: 0; top: 210px;
    text-align: center;
    font-size: 68px;
    color: var(--white);
  }
  .card__shape { position: absolute; inset: 0; }
  .card--back .brand-name {
    left: 60px; top: 215px;
    font-size: 54px;
    color: var(--navy);
  }
  .watermark {
    position: absolute;
    right: -20px; bottom: -40px;
    font-size: 230px;
    font-weight: 700;
    color: var(--watermark);
    opacity: 0.35;
    white-space: nowrap;
  }
  .contact-block { position: absolute; left: 507px; top: 108px; color: var(--white); }
  .person__name { font-size: 40px; font-weight: 700; letter-spacing: 1px; line-height: 1; }
  .person__title { margin-top: 14px; font-size: 27px; font-weight: 500; color: var(--muted); letter-spacing: 1px; line-height: 1; }
  .contact-list { list-style: none; margin-top: 72px; }
  .contact-list__item {
    display: flex; align-items: center;
    height: 37px;
    font-size: 24px; font-weight: 500;
    letter-spacing: 2.5px;
  }
  .contact-list__icon { width: 24px; height: 24px; margin-right: 16px; flex: none; }
</style>
</head>
<body>
  <section class="card card--front">
    <div class="brand-name">KX7 Supply</div>
  </section>

  <section class="card card--back">
    <div class="watermark">KX7</div>
    <svg class="card__shape" viewBox="0 0 861 495" aria-hidden="true">
      <circle cx="40" cy="235" r="413" fill="#ffffff"/>
      <path d="M390 38 A405 405 0 0 1 340 495" fill="none" stroke="#ffffff" stroke-width="11"/>
      <path d="M390 38 A405 405 0 0 1 340 495" fill="none" stroke="#0f93b8" stroke-width="5"/>
    </svg>
    <div class="brand-name">KX7 Supply</div>

    <div class="contact-block">
      <div class="person__name">Dana Reyes</div>
      <div class="person__title">Director</div>
      <ul class="contact-list">
        <li class="contact-list__item">
          <svg class="contact-list__icon" viewBox="0 0 24 24"><path d="M6.6 10.8a15 15 0 0 0 6.6 6.6l2.2-2.2c.3-.3.7-.4 1-.2 1.1.4 2.3.6 3.6.6.6 0 1 .4 1 1V20c0 .6-.4 1-1 1A17 17 0 0 1 3 4c0-.6.4-1 1-1h3.5c.6 0 1 .4 1 1 0 1.3.2 2.5.6 3.6.1.3 0 .7-.2 1z" fill="#0f93b8"/></svg>
          215 555 0147
        </li>
        <li class="contact-list__item">
          <svg class="contact-list__icon" viewBox="0 0 24 24"><rect x="2" y="5" width="20" height="14" fill="#0f93b8"/><path d="M2 5l10 8 10-8" fill="none" stroke="#133758" stroke-width="1.6"/></svg>
          hello@kx7mail.com
        </li>
        <li class="contact-list__item">
          <svg class="contact-list__icon" viewBox="0 0 24 24" fill="none" stroke="#0f93b8" stroke-width="1.8"><circle cx="12" cy="12" r="10"/><ellipse cx="12" cy="12" rx="4.5" ry="10"/><path d="M2 12h20M4 7h16M4 17h16"/></svg>
          www.kx7supply.com
        </li>
      </ul>
    </div>
  </section>
</body>
</html>
```